Book Cover

Book Title: THE QUIET LEDGER
Book Sub Title: Notes on slowing the daily rush and shaping a calmer household rhythm
Vibe: Professional, stylish, trustworthy (high-end men's fashion)
Website (for inspiration): www.brindlequarry.com
Attached: a potential photo to use for the cover, but open to other options (from our website)

```html
<!DOCTYPE html>
<html lang="en">
<head>
<meta charset="utf-8">
<title>The Quiet Ledger — Cover Spread</title>
<link rel="stylesheet" href="https://fonts.googleapis.com/css2?family=Bebas+Neue&family=Raleway:wght@200&family=Roboto+Condensed:wght@400&family=Tenor+Sans&display=swap">
<style>
  :root {
    --stage: #6f6f6f;
    --ink: #111111;
    --paper: #ffffff;
    --back-light: #efe9e2;
    --back-warm: #ddd2c6;
    --front-top: #c9b9a8;
    --front-mid: #9a8a7c;
    --front-deep: #2c3250;
    --spine-block: #000000;
  }
  html, body {
    margin: 0;
    width: 1200px;
    height: 829px;
    overflow: hidden;
    background: var(--stage);
  }
  .canvas {
    position: relative;
    width: 1200px;
    height: 829px;
    overflow: hidden;
    background: var(--stage);
  }
  .spread {
    position: absolute;
    left: 80px;
    top: 14px;
    width: 1040px;
    height: 800px;
    overflow: hidden;
  }

  /* Back cover */
  .back-cover {
    position: absolute;
    left: 0; top: 0;
    width: 548px; height: 800px;
  }
  .back-photo {
    position: absolute;
    inset: 0;
    background: linear-gradient(180deg, var(--back-light) 0%, #e6ddd3 55%, var(--back-warm) 100%);
  }
  .author-bio {
    position: absolute;
    left: 225px;
    top: 40px;
    width: 205px;
    font-family: "Tenor Sans", sans-serif;
    font-size: 14px;
    line-height: 18.8px;
    color: var(--ink);
  }
  .author-bio p { margin: 0 0 18.8px; }

  /* Spine */
  .spine-title-block {
    position: absolute;
    left: 500px; top: 132px;
    width: 41px; height: 178px;
    background: var(--spine-block);
  }
  .spine-title-block span {
    position: absolute;
    left: 50%; top: 50%;
    transform: translate(-50%, -50%) rotate(90deg);
    white-space: nowrap;
    font-family: "Raleway", sans-serif;
    font-weight: 200;
    font-size: 22px;
    letter-spacing: 1px;
    color: var(--paper);
  }
  .spine-main-title {
    position: absolute;
    left: 520px; top: 456px;
    transform: translate(-50%, -50%) rotate(90deg);
    white-space: nowrap;
    font-family: "Bebas Neue", sans-serif;
    font-size: 46px;
    letter-spacing: 18px;
    color: var(--ink);
    line-height: 1;
  }
  .spine-imprint {
    position: absolute;
    left: 500px; top: 707px;
    width: 41px; height: 93px;
    background: var(--spine-block);
  }
  .spine-imprint span {
    position: absolute;
    left: 50%; top: 50%;
    transform: translate(-50%, -50%) rotate(90deg);
    white-space: nowrap;
    font-family: "Tenor Sans", sans-serif;
    font-size: 9px;
    color: var(--paper);
  }

  /* Front cover */
  .front-cover {
    position: absolute;
    left: 548px; top: 0;
    width: 492px; height: 800px;
  }
  .front-photo {
    position: absolute;
    inset: 0;
    background: linear-gradient(180deg, var(--front-top) 0%, var(--front-mid) 40%, #4a4a62 70%, var(--front-deep) 100%);
  }
  .subtitle {
    position: absolute;
    left: 218px; top: 57px;
    width: 230px;
    margin: 0;
    font-family: "Roboto Condensed", sans-serif;
    font-weight: 400;
    font-size: 20px;
    line-height: 26px;
    color: var(--paper);
  }
  .title {
    position: absolute;
    left: 34px; top: 430px;
    margin: 0;
    color: var(--paper);
  }
  .title-lead {
    display: block;
    font-family: "Raleway", sans-serif;
    font-weight: 200;
    font-size: 36px;
    letter-spacing: 21px;
    line-height: 1;
    white-space: nowrap;
  }
  .title-main {
    display: block;
    margin-top: 8px;
    font-family: "Bebas Neue", sans-serif;
    font-weight: 400;
    font-size: 180px;
    line-height: 0.9;
    letter-spacing: 2px;
    transform: scaleY(1.25);
    transform-origin: top left;
    text-shadow: 3px 3px 4px rgba(0, 0, 0, 0.35);
  }
</style>
</head>
<body>
<div class="canvas">
  <div class="spread">
    <section class="back-cover">
      <div class="back-photo" role="img" aria-label="Soft, light-washed photo of the author seated on a wooden stool in a bright loft beside a rack of jackets"></div>
      <div class="author-bio">
        <p>Cal Everholt is the founder of Brindle Quarry and one of the most respected voices in American menswear.</p>
        <p>A Northfield psychology graduate and former college basketball player turned style expert, Cal was named “America’s Best Dressed Real Man” by Harbor Monthly magazine and has been featured in Ledger Weekly, The Coastal Review, The Morning Courier, and hundreds of other publications.</p>
        <p>For over a decade he’s helped thousands of men (and women) from all over the world upgrade their wardrobes and transform the way they dress - with a focus on quality, longevity, and confidence.</p>
        <p>Cal brings a rare combination of style expertise, technical tailoring knowledge, and real-world practicality. He doesn’t just help clients dress better - he helps them feel like the best version of themselves.</p>
      </div>
    </section>

    <div class="spine-title-block"><span>THE QUIET</span></div>
    <div class="spine-main-title">LEDGER</div>
    <div class="spine-imprint"><span>Brindle Quarry</span></div>

    <section class="front-cover">
      <div class="front-photo" role="img" aria-label="Photo of a man in a navy jacket, white shirt and knit tie standing in a bright loft with clothing racks"></div>
      <p class="subtitle">Notes on slowing the daily rush and shaping a calmer household rhythm</p>
      <h1 class="title">
        <span class="title-lead">THE QUIET</span>
        <span class="title-main">LEDGER</span>
      </h1>
    </section>
  </div>
</div>
</body>
</html>
```